Hydraulics Company Business Card Design

Modern business card design for a hydraulics company.
Our company colours are - black, orange and white.
I would like the following contact details included-
Name
Position
Phone number
Email
Website
Street Address

I have attached our company logo.
I would like the back of the card white.

Thank you.

```html
<!DOCTYPE html>
<html lang="en">
<head>
<meta charset="UTF-8">
<title>Kestrelvale Hydraulics – Business Card</title>
<link href="https://fonts.googleapis.com/css2?family=Poppins:wght@400;600;700&display=swap" rel="stylesheet">
<style>
  :root {
    --backdrop: #2c2f34;
    --ink: #0a0a0a;
    --orange: #f59c23;
    --orange-dark: #c97812;
    --paper: #ffffff;
    --text: #1c1c1c;
  }
  * { margin: 0; padding: 0; box-sizing: border-box; }
  html, body {
    width: 1200px;
    height: 985px;
    overflow: hidden;
    background: var(--backdrop);
    font-family: "Poppins", sans-serif;
  }
  .canvas {
    position: relative;
    width: 1200px;
    height: 985px;
  }
  .card {
    position: absolute;
    left: 320px;
    width: 560px;
    height: 320px;
    border-radius: 16px;
    overflow: hidden;
    box-shadow: 0 14px 30px rgba(0, 0, 0, 0.45);
  }

  /* Front card */
  .card--front {
    top: 135px;
    background: var(--paper);
  }
  .front__brand-panel {
    position: absolute;
    left: 0;
    top: 0;
    width: 232px;
    height: 100%;
    background: var(--ink);
  }
  .front__wordmark {
    position: absolute;
    left: 30px;
    top: 52px;
    color: var(--orange);
    font-weight: 700;
    line-height: 1.05;
  }
  .front__wordmark .wordmark__name {
    display: block;
    font-size: 31px;
  }
  .front__wordmark .wordmark__trade {
    display: block;
    font-size: 19px;
    letter-spacing: 2px;
    margin-top: 6px;
    padding-left: 34px;
  }
  .contact-tab {
    position: absolute;
    left: 204px;
    top: 146px;
    width: 56px;
    height: 146px;
    background: var(--orange);
    border-radius: 0 12px 12px 12px;
    display: flex;
    flex-direction: column;
    align-items: center;
    justify-content: center;
    gap: 14px;
  }
  .contact-tab__fold {
    position: absolute;
    left: 0;
    top: -9px;
    width: 0;
    height: 0;
    border-left: 9px solid transparent;
    border-bottom: 9px solid var(--orange-dark);
  }
  .contact-tab__icon {
    width: 26px;
    height: 26px;
    border-radius: 50%;
    background: var(--ink);
    display: flex;
    align-items: center;
    justify-content: center;
  }
  .contact-tab__icon svg { width: 14px; height: 14px; }

  .front__details {
    position: absolute;
    left: 286px;
    top: 50px;
    color: var(--text);
  }
  .person__name {
    color: var(--orange);
    font-weight: 700;
    font-size: 21px;
    letter-spacing: 0.5px;
    text-transform: uppercase;
    line-height: 1.1;
  }
  .person__role {
    font-size: 14px;
    margin-bottom: 16px;
  }
  .details__line {
    font-size: 14px;
    line-height: 1.55;
  }
  .details__line--gap { margin-top: 10px; }

  /* Back card */
  .card--back {
    top: 530px;
    background: var(--orange);
    display: flex;
    align-items: center;
    justify-content: center;
  }
  .back__wordmark {
    color: var(--paper);
    font-weight: 700;
    line-height: 1;
    text-align: left;
  }
  .back__wordmark .wordmark__name {
    display: block;
    font-size: 58px;
  }
  .back__wordmark .wordmark__trade {
    display: block;
    font-size: 32px;
    letter-spacing: 4px;
    margin-top: 10px;
    padding-left: 64px;
  }
</style>
</head>
<body>
<main class="canvas">

  <section class="card card--front" aria-label="Business card front">
    <div class="front__brand-panel">
      <div class="front__wordmark">
        <span class="wordmark__name">Kestrelvale</span>
        <span class="wordmark__trade">HYDRAULICS</span>
      </div>
    </div>

    <div class="contact-tab">
      <span class="contact-tab__fold"></span>
      <span class="contact-tab__icon" aria-label="Phone">
        <svg viewBox="0 0 24 24"><path fill="#fff" d="M6.6 10.8a15.1 15.1 0 0 0 6.6 6.6l2.2-2.2a1 1 0 0 1 1-.25 11.4 11.4 0 0 0 3.6.57 1 1 0 0 1 1 1V20a1 1 0 0 1-1 1A17 17 0 0 1 3 4a1 1 0 0 1 1-1h3.5a1 1 0 0 1 1 1c0 1.25.2 2.46.57 3.6a1 1 0 0 1-.25 1z"/></svg>
      </span>
      <span class="contact-tab__icon" aria-label="Email">
        <svg viewBox="0 0 24 24"><rect x="3" y="5" width="18" height="14" rx="1.5" fill="none" stroke="#fff" stroke-width="2"/><path d="M3.5 6l8.5 7 8.5-7" fill="none" stroke="#fff" stroke-width="2"/></svg>
      </span>
      <span class="contact-tab__icon" aria-label="Website">
        <svg viewBox="0 0 24 24"><rect x="3" y="4" width="18" height="13" rx="1.5" fill="none" stroke="#fff" stroke-width="2"/><path d="M8 21h8M12 17v4" stroke="#fff" stroke-width="2"/></svg>
      </span>
    </div>

    <div class="front__details">
      <p class="person__name">Marcus Hale</p>
      <p class="person__role">Director</p>
      <p class="details__line">4820 W. Canal Rd.</p>
      <p class="details__line">Suite 210, Arizona 85001</p>
      <p class="details__line details__line--gap">+1 555-014-2780</p>
      <p class="details__line">info@kestrelvale.com</p>
      <p class="details__line">www.kestrelvale.com</p>
    </div>
  </section>

  <section class="card card--back" aria-label="Business card back">
    <div class="back__wordmark">
      <span class="wordmark__name">Kestrelvale</span>
      <span class="wordmark__trade">HYDRAULICS</span>
    </div>
  </section>

</main>
</body>
</html>
```